Postcard Design

Looking for a postcard to inform of a new email address and inform professionals who refer to us of all our services.

Motto - Working together with families, schools, physicians, and counselors to ensure children exceed

Work with:
Children
Teens
College Students
Adults

Specailize in:
LD
ADHD
IEP
Autism
Tourettes
Depression
Aniexity Disorders
Bi-polar
RAD
Section 504's
Apraxia
Speech Language Disorders
IEE (Independant Education Evaluations)

Target Market(s)

Physicians, Counselors

Industry/Entity Type

College

Logo Text

Vostrick Inc.

Logo styles of interest
Abstract Logo
Wordmark Logo
Lettermark Logo
Requirements
Must have
• postcard must advertise business/services
postcard must inform past andpotential customers of new email address. vostrick@vostrickinc.example.com
Nice to have
• list services
Should not have
• Dr. is not a MD. Dr. is a PHD.

```html
<!DOCTYPE html>
<html lang="en">
<head>
<meta charset="utf-8">
<title>Vostrick Inc. Postcard</title>
<link rel="stylesheet" href="https://fonts.googleapis.com/css2?family=Noto+Serif:wght@300;400&family=Oswald:wght@400;500&family=Arimo&display=swap">
<style>
  :root {
    --backdrop: #4a4a4a;
    --paper: #ffffff;
    --blue: #00a8dc;
    --brand-blue: #0a86c9;
    --orange: #f08a2e;
    --purple: #b86fae;
    --green: #63b944;
    --magenta: #b34c9b;
    --ink: #555555;
    --rule: #444444;
    --number: #ffe84a;
  }
  * { box-sizing: border-box; margin: 0; padding: 0; }
  html, body { width: 950px; height: 1200px; overflow: hidden; }
  body { background: var(--backdrop); position: relative; font-family: 'Noto Serif', serif; }

  .card { position: absolute; background: var(--paper); overflow: hidden; }
  .card--front { left: 47px; top: 26px; width: 862px; height: 574px; }
  .card--back { left: 51px; top: 621px; width: 844px; height: 563px; }

  .motto-panel {
    position: absolute; left: 0; top: 0; width: 346px; height: 345px;
    background: var(--blue); color: #fff;
    display: flex; align-items: center; justify-content: center;
    padding: 0 12px 20px;
  }
  .motto { font-weight: 300; font-size: 29px; line-height: 36px; text-align: center; letter-spacing: 0.2px; }

  .brand { position: absolute; left: 391px; top: 70px; }
  .brand__name { font-size: 26px; color: var(--brand-blue); letter-spacing: 0.5px; line-height: 32px; }
  .brand__person, .brand__role { font-size: 17px; color: var(--ink); line-height: 23px; }

  .services {
    position: absolute; left: 323px; top: 305px; width: 539px; height: 269px;
    display: grid; grid-template-columns: repeat(6, 1fr); grid-template-rows: repeat(3, 1fr);
    outline: 6px solid var(--paper);
  }
  .tile {
    position: relative; display: flex; align-items: center; justify-content: center;
    font-family: 'Oswald', sans-serif; font-weight: 500; color: #fff;
    font-size: 17px; line-height: 20px; text-align: center;
  }
  .tile--orange { background: var(--orange); }
  .tile--blue { background: var(--blue); }
  .tile--purple { background: var(--purple); }
  .tile--green { background: var(--green); }
  .tile--photo-warm { background: linear-gradient(160deg, #d9b49a, #8a6a5a 60%, #c44b3f); }
  .tile--photo-light { background: linear-gradient(160deg, #e6e8ea, #b89a86 55%, #5a4b44); }
  .tile--photo-cool { background: linear-gradient(160deg, #dfe4ea, #c9a58e 55%, #e79aa8); }
  .tile__small { font-size: 10px; line-height: 12px; display: block; }
  .tile__num {
    position: absolute; font-family: 'Arimo', sans-serif; font-weight: 400;
    font-size: 18px; color: var(--number); line-height: 1;
  }
  .tile__num--top { top: 5px; left: 0; right: 0; text-align: center; }
  .tile__num--bottom { bottom: 2px; left: 0; right: 0; text-align: center; }
  .tile__num--dark { color: #111; }
  .tile__label--low { margin-top: 10px; }

  .connect { position: absolute; left: 43px; top: 378px; width: 270px; }
  .connect__title { font-family: 'Oswald', sans-serif; font-size: 18px; color: var(--brand-blue); padding-left: 2px; }
  .connect__rule { height: 2px; width: 200px; margin: 8px 0 10px 9px; background: linear-gradient(90deg, transparent, var(--brand-blue) 30%, var(--brand-blue) 70%, transparent); }
  .contact-list { list-style: none; }
  .contact {
    display: flex; align-items: center; gap: 4px; height: 33px;
    font-family: 'Oswald', sans-serif; font-size: 16px; color: var(--ink);
  }
  .contact__icon { width: 18px; height: 18px; flex: none; }

  .return-address { position: absolute; left: 0; top: 28px; width: 438px; text-align: center; font-size: 18px; line-height: 29.3px; color: var(--ink); }
  .return-address__name { color: var(--brand-blue); }
  .divider { position: absolute; left: 435px; top: 30px; width: 1px; height: 478px; background: var(--rule); }
  .address-line { position: absolute; left: 488px; width: 312px; height: 1px; background: var(--rule); }

  .notice { position: absolute; left: 0; top: 455px; width: 438px; text-align: center; }
  .notice__text { font-family: 'Arimo', sans-serif; font-size: 16px; color: #111; line-height: 22px; }
  .notice__email { font-family: 'Oswald', sans-serif; font-weight: 500; font-size: 21px; color: var(--magenta); line-height: 28px; }

  .color-bar { position: absolute; left: 0; top: 517px; height: 46px; display: flex; }
  .color-bar span { display: block; height: 100%; }
</style>
</head>
<body>

<section class="card card--front">
  <div class="motto-panel">
    <p class="motto">Working together with families, schools, physicians, and counselors to ensure children exceed</p>
  </div>

  <div class="brand">
    <h1 class="brand__name">VOSTRICK, INC</h1>
    <p class="brand__person">Martin R. Vostrick, Ph.D</p>
    <p class="brand__role">Education Specialist</p>
  </div>

  <div class="connect">
    <p class="connect__title">Connect with Vostrick INC at</p>
    <div class="connect__rule"></div>
    <ul class="contact-list">
      <li class="contact">
        <svg class="contact__icon" viewBox="0 0 18 18"><circle cx="9" cy="9" r="9" fill="#1a9ad6"/><rect x="4.5" y="6" width="9" height="6.5" fill="none" stroke="#fff" stroke-width="1.2"/><path d="M4.5 6 9 9.8 13.5 6" fill="none" stroke="#fff" stroke-width="1.2"/></svg>
        vostrick@vostrickinc.example.com
      </li>
      <li class="contact">
        <svg class="contact__icon" viewBox="0 0 18 18"><circle cx="9" cy="9" r="9" fill="#b86fae"/><circle cx="9" cy="9" r="5" fill="none" stroke="#fff" stroke-width="1"/><ellipse cx="9" cy="9" rx="2.2" ry="5" fill="none" stroke="#fff" stroke-width="1"/><path d="M4 9h10" stroke="#fff" stroke-width="1"/></svg>
        vostrickinc.example.com
      </li>
      <li class="contact">
        <svg class="contact__icon" viewBox="0 0 18 18"><circle cx="9" cy="9" r="9" fill="#2d5aa0"/></svg>
        Vostrick-Inc/100200300400
      </li>
      <li class="contact">
        <svg class="contact__icon" viewBox="0 0 18 18"><circle cx="9" cy="9" r="9" fill="#c4262e"/></svg>
        Drvostrick
      </li>
    </ul>
  </div>

  <div class="services">
    <div class="tile tile--orange"><span class="tile__num tile__num--top">1</span><span class="tile__label--low">LD</span></div>
    <div class="tile tile--photo-warm" role="img" aria-label="Photo of a group of smiling teenagers"><span class="tile__num tile__num--top" style="color:#1a9ad6">2</span></div>
    <div class="tile tile--purple"><span class="tile__num tile__num--top">3</span><span class="tile__label--low">ADHD</span></div>
    <div class="tile tile--blue"><span class="tile__num tile__num--top">4</span><span class="tile__label--low">IEP</span></div>
    <div class="tile tile--photo-light" role="img" aria-label="Photo of a college student holding books"><span class="tile__num tile__num--top tile__num--dark" style="left:auto;right:12px;top:10px">5</span></div>
    <div class="tile tile--green"><span class="tile__num tile__num--top">6</span><span class="tile__label--low">Autism</span></div>

    <div class="tile tile--photo-warm" role="img" aria-label="Photo of a smiling young woman"><span class="tile__num tile__num--top" style="left:auto;right:14px">7</span></div>
    <div class="tile tile--blue"><span class="tile__num tile__num--top">8</span><span class="tile__label--low">Tourettes</span></div>
    <div class="tile tile--photo-cool" role="img" aria-label="Photo of happy children lying together"><span class="tile__num tile__num--top tile__num--dark" style="left:6px;right:auto">9</span></div>
    <div class="tile tile--orange"><span class="tile__num tile__num--top">10</span><span class="tile__label--low">Depression</span></div>
    <div class="tile tile--blue"><span class="tile__num tile__num--top" style="top:8px">11</span><span class="tile__label--low">Anxiety<br>Disorders</span></div>
    <div class="tile tile--purple"><span class="tile__num tile__num--top">12</span><span class="tile__label--low">Bi-polar</span></div>

    <div class="tile tile--green"><span>RAD</span><span class="tile__num tile__num--bottom">13</span></div>
    <div class="tile tile--purple"><span style="margin-bottom:12px">Section<br>504's</span><span class="tile__num tile__num--bottom">14</span></div>
    <div class="tile tile--blue"><span style="margin-bottom:12px">Apraxia</span><span class="tile__num tile__num--bottom" style="bottom:10px">15</span></div>
    <div class="tile tile--photo-light" role="img" aria-label="Photo of a smiling adult couple"><span class="tile__num tile__num--bottom tile__num--dark" style="left:auto;right:22px;bottom:6px">16</span></div>
    <div class="tile tile--purple"><span style="margin-bottom:12px">Speech<br>Language<br>Disorders</span><span class="tile__num tile__num--bottom" style="bottom:-2px">17</span></div>
    <div class="tile tile--orange"><span style="margin-bottom:16px">IEE<span class="tile__small">(Independant<br>Education<br>Evaluations)</span></span><span class="tile__num tile__num--bottom" style="bottom:-2px">18</span></div>
  </div>
</section>

<section class="card card--back">
  <address class="return-address" style="font-style:normal">
    <p class="return-address__name">Vostrick INC</p>
    <p>420 Linden Avenue</p>
    <p>Suite 104</p>
    <p>Alder Falls, NY&nbsp;&nbsp;10999</p>
    <p>(555) 010-4821</p>
  </address>

  <div class="divider"></div>
  <div class="address-line" style="top:258px"></div>
  <div class="address-line" style="top:304px"></div>
  <div class="address-line" style="top:351px"></div>
  <div class="address-line" style="top:390px"></div>

  <div class="notice">
    <p class="notice__text">Please note new email address</p>
    <p class="notice__email">vostrick@vostrickinc.example.com</p>
  </div>

  <div class="color-bar">
    <span style="width:101px;background:var(--purple)"></span>
    <span style="width:179px;background:var(--green)"></span>
    <span style="width:51px;background:var(--orange)"></span>
    <span style="width:106px;background:var(--blue)"></span>
  </div>
</section>

</body>
</html>
```